Web Design Project for an operational risk management consulting company

Website is for a consulting company specialising in operational risk management. Our specialist areas include crisis and emergency management, community engagement, safety and security. We work internationally, generally in high hazard environments. We are a highly ethical and professional company which prides itself on delivering a strong level of customer service.

As a company we recognise that the key to keeping people safe is ensuring that they work in an ethical and sustainable manner. Therefore we are as much about soft skills as we are about hard skills. We would like our website and supporting images to reflect this.
We have worked throughout Africa and the Middle east, as well as Asia pacific. An international flavour to the website would also be great.
Background images on www.corvellpartnersglobal.example are a good example of what we are thinking of, though very open to fresh ideas.

Target Market(s)

Our customers are generally medium to large organisations who work internationally. We would like to also support more not for profits and non government organisations who work in hazardous environments

Industry/Entity Type

It Company

Number of Pages Required

5+ page

Font styles to use
Sans Serif

Requirements
Must have
• Easy to edit by non IT people
• Section for blogs/news updates
• Pages should include:
• (A) home page
• (B) about us
• (C) services
• (D) contact
• (E) insights
Nice to have
• An international and professional theme. Some gritty images that symbolise the risks associated with working in unstable environments, as well as some human ones and that of the environment
Should not have
• Cartoonish or generic images
• Not focus on traditional physical security aspects

```html
<!DOCTYPE html>
<html lang="en">
<head>
<meta charset="utf-8">
<title>Halden Risk</title>
<link href="https://fonts.googleapis.com/css2?family=Open+Sans:wght@400;600;700&family=Roboto:wght@400;500&display=swap" rel="stylesheet">
<style>
:root{
  --bg-top:#e9e9e9;
  --bg-bottom:#b9b9b9;
  --page:#ffffff;
  --ink:#333333;
  --muted:#6b6b6b;
  --brand:#1d6fa5;
  --brand-dark:#145a88;
  --nav:#2f2f2f;
  --footer:#262626;
  --accent:#e98a2b;
  --hero-a:#4d7d9e;
  --hero-b:#b08a62;
}
*{box-sizing:border-box;margin:0;padding:0}
html,body{width:853px;height:1200px;overflow:hidden}
body{background:linear-gradient(180deg,var(--bg-top),var(--bg-bottom));font-family:'Open Sans',Arial,sans-serif;color:var(--ink);position:relative}
.page{position:absolute;left:176px;top:0;width:492px;height:1200px;background:var(--page);box-shadow:0 0 12px rgba(0,0,0,.25)}
.header{height:72px;position:relative;border-top:3px solid var(--brand)}
.brand{position:absolute;left:16px;top:12px;display:flex;align-items:center;gap:8px}
.brand-dot{width:30px;height:30px;border-radius:50%;background:var(--brand)}
.brand-name{font-size:14px;font-weight:700;color:var(--brand)}
.contact{position:absolute;right:18px;top:26px;display:flex;gap:18px;font-size:10px;color:var(--ink)}
.contact span{display:flex;align-items:center;gap:6px}
.contact i{width:14px;height:14px;border-radius:50%;background:var(--brand);display:inline-flex;align-items:center;justify-content:center}
.nav{height:26px;background:var(--nav);display:flex;align-items:center;position:relative}
.nav a{color:#fff;font-size:10px;text-decoration:none;padding:0 10px;line-height:26px}
.nav a.active{background:var(--brand)}
.search{position:absolute;right:10px;top:6px;width:66px;height:14px;background:#fff;border-radius:2px;font-size:7px;color:#999;padding-left:4px;line-height:14px}
.hero{height:312px;position:relative;background:linear-gradient(160deg,var(--hero-a) 0%,#8fa9b8 40%,var(--hero-b) 100%);overflow:hidden}
.hero h1{position:absolute;left:20px;top:108px;width:230px;color:#fff;font-family:'Roboto',sans-serif;font-weight:500;font-size:22px;line-height:28px;text-shadow:0 1px 3px rgba(0,0,0,.4)}
.hero svg{position:absolute;left:0;bottom:0}
.section{position:absolute;left:16px;right:16px}
h2{font-family:'Roboto',sans-serif;font-weight:400;font-size:20px;color:var(--ink)}
p{font-size:8px;line-height:11px;color:var(--muted)}
.btn{display:inline-block;background:var(--brand);color:#fff;font-size:8px;padding:4px 9px;border-radius:2px}
.welcome{top:420px;height:180px}
.welcome .text{width:225px}
.welcome p{margin:10px 0 10px}
.video{position:absolute;right:0;top:-6px;width:210px;height:128px;border:3px solid #f0c9a8;background:linear-gradient(135deg,#c98f5e,#8a6a4e)}
.video .bar{position:absolute;left:0;right:0;bottom:0;height:12px;background:var(--brand-dark)}
.services{top:610px;height:230px}
.title-row{display:flex;align-items:center;gap:6px}
.arrows{display:flex;gap:3px}
.arrows i{width:10px;height:10px;background:#555;display:block}
.svc-grid{position:absolute;top:34px;left:0;width:290px;display:grid;grid-template-columns:1fr 1fr;gap:12px 14px}
.svc{display:flex;gap:6px}
.svc .thumb{width:52px;height:78px;flex:none}
.svc h3{font-size:9px;font-weight:600;margin-bottom:3px}
.svc p{font-size:7px;line-height:9px;margin-bottom:5px}
.testimonial{position:absolute;right:0;top:16px;width:160px;height:178px;background:var(--brand);color:#fff;text-align:center;padding-top:8px}
.testimonial h3{font-family:'Roboto',sans-serif;font-weight:400;font-size:15px}
.avatar{width:50px;height:50px;border-radius:50%;background:linear-gradient(#d9b89a,#a07f66);border:3px solid #fff;margin:8px auto}
.testimonial p{color:#fff;padding:0 14px}
.testimonial .who{font-size:8px;margin-top:6px;color:#cfe4f3}
.news{top:862px}
.news-grid{margin-top:14px;display:grid;grid-template-columns:repeat(3,1fr);gap:12px}
.card .img{height:68px;margin-bottom:6px}
.card h3{font-size:9px;font-weight:600}
.card .date{font-size:7px;color:var(--accent);margin:2px 0}
.card p{font-size:7px;line-height:9px;margin-bottom:5px}
.footer{position:absolute;left:0;right:0;bottom:0;height:100px;background:var(--footer);color:#ddd;text-align:center;padding-top:14px}
.social{display:flex;justify-content:center;gap:6px}
.social i{width:16px;height:16px;border-radius:50%;background:#777;display:block}
.fnav{margin-top:14px;display:flex;justify-content:center;gap:12px;font-size:8px}
.copy{font-size:7px;color:#999;margin-top:6px}
</style>
</head>
<body>
<div class="page">
  <header class="header">
    <div class="brand"><span class="brand-dot"></span><span class="brand-name">Halden Risk</span></div>
    <div class="contact">
      <span><i><svg width="8" height="6" viewBox="0 0 8 6"><rect x=".5" y=".5" width="7" height="5" fill="none" stroke="#fff"/><path d="M.5 .5 4 3.5 7.5 .5" fill="none" stroke="#fff"/></svg></i>haldenrisk.example</span>
      <span><i><svg width="8" height="8" viewBox="0 0 8 8"><path d="M1 1c1-1 2 0 2 1L2 3c1 2 2 3 3 3l1-1c1 0 2 1 1 2-3 2-8-3-6-6z" fill="#fff"/></svg></i>1-800-555-0142</span>
    </div>
  </header>
  <nav class="nav">
    <a class="active">Home</a><a>About Us</a><a>Service</a><a>News</a><a>Testimonial</a><a>Contact Us</a>
    <div class="search">Search</div>
  </nav>
  <section class="hero" role="img" aria-label="Traveller carrying a load on a rocky coastal trail under a blue sky">
    <h1>Life is either a daring adventure or nothing at all</h1>
    <svg width="492" height="20" viewBox="0 0 492 20"><path d="M0 20V10Q246-6 492 10V20Z" fill="#fff"/><path d="M0 10Q246-6 492 10" fill="none" stroke="var(--brand)" stroke-width="3"/></svg>
  </section>

  <section class="section welcome">
    <div class="text">
      <h2>Welcome Our Company</h2>
      <p>It is a long established fact that a reader will be distracted by the readable content of a page when looking at its layout. The point of using Lorem Ipsum is that it has a more-or-less normal distribution of letters, as opposed to using Content here, content here.</p>
      <span class="btn">View More</span>
    </div>
    <div class="video" role="img" aria-label="Video still of a field team in a desert setting"><div class="bar"></div></div>
  </section>

  <section class="section services">
    <div class="title-row"><h2>Our Services</h2><div class="arrows"><i></i><i></i></div></div>
    <div class="svc-grid">
      <div class="svc"><div class="thumb" role="img" aria-label="Workers in a village" style="background:linear-gradient(#b88a5e,#6f5a44)"></div><div><h3>Lorem Ipsum</h3><p>Proin gravida nibh vel velit auctor aliquet, sollicitudin lorem.</p><span class="btn">Read More</span></div></div>
      <div class="svc"><div class="thumb" role="img" aria-label="Aid workers meeting" style="background:linear-gradient(#8fa3b0,#4f6470)"></div><div><h3>Lorem Ipsum</h3><p>Proin gravida nibh vel velit auctor aliquet, sollicitudin lorem.</p><span class="btn">Read More</span></div></div>
      <div class="svc"><div class="thumb" role="img" aria-label="Community gathering" style="background:linear-gradient(#c9a07a,#7c5d45)"></div><div><h3>Lorem Ipsum</h3><p>Proin gravida nibh vel velit auctor aliquet, sollicitudin lorem.</p><span class="btn">Read More</span></div></div>
      <div class="svc"><div class="thumb" role="img" aria-label="Safety training session" style="background:linear-gradient(#a8b4a0,#5e6b58)"></div><div><h3>Lorem Ipsum</h3><p>Proin gravida nibh vel velit auctor aliquet, sollicitudin lorem.</p><span class="btn">Read More</span></div></div>
    </div>
    <aside class="testimonial">
      <h3>Testimonial</h3>
      <div class="avatar" role="img" aria-label="Client portrait"></div>
      <p>It is a long established fact that a reader will be distracted by the readable content of a page.</p>
      <div class="who">Selwyn Carrow</div>
    </aside>
  </section>

  <section class="section news">
    <div class="title-row"><h2>News</h2><div class="arrows"><i></i><i></i></div></div>
    <div class="news-grid">
      <article class="card"><div class="img" role="img" aria-label="Camels crossing desert dunes" style="background:linear-gradient(#e3b77c,#b07a45)"></div><h3>Lorem Ipsum is simply dummy</h3><div class="date">September 28,2015</div><p>There are many variations of passages of Lorem Ipsum.</p><span class="btn">Read More</span></article>
      <article class="card"><div class="img" role="img" aria-label="Field workers outdoors" style="background:linear-gradient(#9fb08a,#6a6b50)"></div><h3>Lorem Ipsum is simply dummy</h3><div class="date">September 28,2015</div><p>There are many variations of passages of Lorem Ipsum.</p><span class="btn">Read More</span></article>
      <article class="card"><div class="img" role="img" aria-label="Desert market scene" style="background:linear-gradient(#d19a66,#8a5a38)"></div><h3>Lorem Ipsum is simply dummy</h3><div class="date">September 28,2015</div><p>There are many variations of passages of Lorem Ipsum.</p><span class="btn">Read More</span></article>
    </div>
  </section>

  <footer class="footer">
    <div class="social"><i></i><i></i><i></i><i></i><i></i><i></i></div>
    <div class="fnav"><span>HOME</span><span>ABOUT US</span><span>SERVICE</span><span>NEWS</span><span>CONTACT US</span></div>
    <div class="copy">© 2015 Halden Risk. All rights reserved.</div>
  </footer>
</div>
</body>
</html>
```